Business card design needed

Marketing Communications

Target Market(s)

prospective clients in the marketing communications industry

Industry/Entity Type

Business

Contact Information for Business Card

merel vasko
Marketing Communications
tolupar@quennet.com
0462 815947

Logo Text

merel vasko

Logo styles of interest
Abstract Logo
Requirements
Must have
• An appropriate abstract logo. only a one or two colour design
Nice to have
• Logo to portray the growth of a marketing brief
Should not have
• no more than two colours maximum

```html
<!DOCTYPE html>
<html lang="en">
<head>
<meta charset="utf-8">
<title>Merel Vasko — Business Card</title>
<link rel="stylesheet" href="https://fonts.googleapis.com/css2?family=Cinzel+Decorative:wght@400&family=Crimson+Text:wght@400&display=swap">
<style>
  :root {
    --backdrop: #2b2b2b;
    --card: #050505;
    --ink: #ffffff;
    --ink-soft: #ececec;
  }
  * { margin: 0; padding: 0; box-sizing: border-box; }
  html, body {
    width: 1200px;
    height: 900px;
    overflow: hidden;
    background: var(--backdrop);
  }
  .canvas {
    width: 1200px;
    height: 900px;
    display: flex;
    align-items: center;
    justify-content: center;
  }
  .business-card {
    width: 840px;
    height: 480px;
    background: var(--card);
    display: flex;
    flex-direction: column;
    align-items: center;
    justify-content: center;
    padding-bottom: 20px;
    color: var(--ink);
    text-align: center;
  }
  .identity {
    display: flex;
    flex-direction: column;
    align-items: center;
  }
  .holder-name {
    font-family: "Cinzel Decorative", serif;
    font-weight: 400;
    font-size: 56px;
    letter-spacing: 0;
    line-height: 1;
    text-transform: uppercase;
  }
  .holder-role {
    font-family: "Crimson Text", serif;
    font-size: 23px;
    color: var(--ink-soft);
    margin-top: 8px;
  }
  .contact {
    margin-top: 22px;
    font-family: "Crimson Text", serif;
    font-size: 25px;
    line-height: 1.25;
    color: var(--ink-soft);
    font-style: normal;
  }
  .contact-phone { letter-spacing: 1.5px; }
</style>
</head>
<body>
  <main class="canvas">
    <section class="business-card" aria-label="Business card front">
      <div class="identity">
        <h1 class="holder-name">Merel Vasko</h1>
        <p class="holder-role">Marketing Communications</p>
      </div>
      <address class="contact">
        <div class="contact-phone">0462 815947</div>
        <div class="contact-email">tolupar@quennet.com</div>
      </address>
    </section>
  </main>
</body>
</html>
```